Coastal Silken Hair Weaves needs a packaging design

We need a packaging design for a new hair extension company based in Edmonton, Alberta called Velvet Crest. Our packaging should communicate high quality, luxurious hair that will never tangle or dry out. The product will be marketed to salon professionals as well as clients. We would like to see designs that include but not restricted to the colours gold black and white.
Updates

Reason: Although we were very impressed with the designs that came though thus far, we are hoping to receive a few more ideas before making a final decision. Thank you!

Target Market(s)

Women and beauty industry professionals. High end market.

Industry/Entity Type

Hair

Requirements
Must have
• "Highest quality 100% Remi hair!" should be written on the front of the package. In addition, we would like to add text to the back of the packaging as follows:
• Hair Collection and Color Processing:
• Only the highest quality hair is selected which ensures high moisture and nutrient content
• The hair is directly cut from the donor which ensures that the hair cuticle remains intact and always tangle-free
• No chemicals are used in dyeing the hair
• The hair will never fade due to the mild and healthy herbal extract used in the dyeing process which gently penetrates to the inner core of the hair
• Care Instructions:
• Velvet Crest provides only the highest in quality Remi hair that demands very little care to maintain it’s luxurious feel.
• Use a proper extension bristle brush
• Wash the hair with a sulfate-free shampoo and follow with a moisturizing conditioner that is formulated for hair extensions
• Do not apply any type of chemicals to the hair
• We proudly show our immense passion for delivering superior quality in our full product line.
• We insist that it is important for you to know and understand what you are purchasing in your hair extensions. We guarantee the highest quality of our products.
• Velvet Crest is strongly committed to serving their clients with utmost integrity, believing in a foundation of personal and professional ethics and our 20 years service in the beauty industry.
Nice to have
• I would like the background to be white with the "C" in gold. My concern is that this may look too plain, but with that said, I don't want the design to be too busy. Keeping it classy is my main goal.

```html
<!DOCTYPE html>
<html lang="en">
<head>
<meta charset="UTF-8">
<title>Velvet Crest – Hair Extension Package</title>
<link href="https://fonts.googleapis.com/css2?family=Arimo:wght@400;700&display=swap" rel="stylesheet">
<style>
  :root {
    --paper: #ffffff;
    --ink: #0d0d0d;
    --gold-dark: #a67c2e;
    --gold-mid: #d4b062;
    --gold-light: #eed9a0;
    --hair-dark: #060606;
    --hair-mid: #1c1c1c;
    --hair-sheen: #303030;
    --text-light: #f5f5f5;
  }
  html, body {
    margin: 0;
    padding: 0;
    width: 1200px;
    height: 2448px;
    overflow: hidden;
    background: var(--paper);
  }
  .canvas {
    position: relative;
    width: 1200px;
    height: 2448px;
    background: var(--paper);
    font-family: "Arimo", Arial, sans-serif;
  }
  .package {
    position: absolute;
    left: 384px;
    top: 288px;
    width: 444px;
  }
  .header-card {
    position: relative;
    width: 444px;
    height: 300px;
    background: var(--paper);
  }
  .header-card svg {
    position: absolute;
    inset: 0;
  }
  .brand-name {
    position: absolute;
    left: 0;
    right: 0;
    top: 178px;
    text-align: center;
    font-size: 40px;
    font-weight: 400;
    color: var(--ink);
    letter-spacing: 0.5px;
  }
  .gold-band {
    background: linear-gradient(90deg, var(--gold-dark) 0%, var(--gold-mid) 30%, var(--gold-light) 55%, var(--gold-mid) 75%, var(--gold-dark) 100%);
    color: var(--paper);
    text-align: center;
  }
  .quality-strip {
    height: 24px;
    line-height: 24px;
    font-size: 13px;
    letter-spacing: 0.4px;
    text-transform: uppercase;
    white-space: nowrap;
  }
  .features {
    background: var(--ink);
    color: var(--text-light);
    height: 139px;
    box-sizing: border-box;
    padding-top: 6px;
    margin: 0;
    list-style: none;
    text-align: center;
    font-size: 23px;
    line-height: 26.5px;
  }
  .about-strip {
    height: 65px;
    box-sizing: border-box;
    padding-top: 6px;
    font-size: 12px;
    line-height: 15px;
  }
  .hair-sample {
    width: 437px;
    height: 1459px;
    margin-left: 5px;
    background:
      repeating-linear-gradient(92deg, rgba(255,255,255,0.035) 0 2px, transparent 2px 7px),
      linear-gradient(90deg, var(--hair-dark) 0%, var(--hair-mid) 25%, var(--hair-sheen) 45%, var(--hair-mid) 60%, var(--hair-dark) 85%, var(--hair-mid) 100%);
  }
</style>
</head>
<body>
<div class="canvas">
  <div class="package">
    <div class="header-card">
      <svg width="444" height="300" viewBox="0 0 444 300" aria-hidden="true">
        <path d="M2 2 H168 V34 H228 V62 H252 V2 H442 V298 H2 Z" fill="none" stroke="#0d0d0d" stroke-width="4" stroke-linejoin="miter"/>
        <circle class="shade-swatch" cx="360" cy="67" r="38" fill="#000"/>
      </svg>
      <div class="brand-name">Velvet Crest</div>
    </div>
    <div class="gold-band quality-strip">The highest quality 100% Remi human hair</div>
    <ul class="features">
      <li>Double drawn, single weft</li>
      <li>All cuticle in same direction</li>
      <li>No tangling, shedding, or matting</li>
      <li>Natural textre shine and movement</li>
      <li>Long lasting, durable hair.</li>
    </ul>
    <div class="gold-band about-strip">
      VELVET CREST is a Canadian based wholesaler<br>
      of human hair and hair products.<br>
      We pride ourselves on providing the highest quality.
    </div>
    <div class="hair-sample" role="img" aria-label="Photograph of straight, glossy jet black hair extension weft"></div>
  </div>
</div>
</body>
</html>
```